Business card, postcard, pocket folder

We are a real estate team and have had a new logo designed. From this, we need the following deliverables:- Business Cards (double-sided)- Just Listed / Just Sold Postcards (double-sided)- Pocket Folder. See logo attached.More work possible for the winning designer.
There are 5 members of the team, so head shots should be easily changed and possible for a group photo might be a good idea for the pocket folder but not 100% neccessary.
Target Market(s)
Real estate
Industry/Entity Type
Real Estate
Font styles to use
Serif
Sans Serif
Requirements
Must have
- Business cards and postcards must have a head shot on them.

```html
<!DOCTYPE html>
<html lang="en">
<head>
<meta charset="utf-8">
<title>Harrowgate Group – Pocket Folder</title>
<link href="https://fonts.googleapis.com/css2?family=Montserrat:wght@400;600;700&family=Oswald:wght@600;700&display=swap" rel="stylesheet">
<style>
  :root{
    --bg:#d9d9d9;
    --ink:#252525;
    --red:#c8142b;
    --red-dark:#a90f22;
    --navy:#2b3a92;
    --white:#ffffff;
    --paper:#f4f4f4;
    --muted:#bfbfbf;
    --grey-avatar:#e3e3e3;
  }
  *{box-sizing:border-box;margin:0;padding:0}
  html,body{width:1200px;height:1200px;overflow:hidden}
  body{background:var(--bg);font-family:"Montserrat",sans-serif;position:relative}

  .spread{position:absolute;left:195px;width:780px;height:520px;display:flex;box-shadow:0 10px 30px rgba(0,0,0,.18)}
  .spread--outside{top:45px}
  .spread--inside{top:630px}
  .panel{position:relative;width:390px;height:520px;overflow:hidden}

  .view-label{position:absolute;left:1005px;font-family:"Montserrat",sans-serif;font-size:26px;color:#1d1d1d;letter-spacing:1px}
  .view-label--outside{top:200px}
  .view-label--inside{top:770px}

  /* back panel */
  .back{background:var(--ink);color:var(--white);padding:44px 26px 0 0}
  .team-tag{display:inline-block;background:var(--red);font-family:"Oswald",sans-serif;font-weight:600;font-size:14px;padding:5px 26px 5px 14px;clip-path:polygon(0 0,100% 0,90% 100%,0 100%)}
  .team-list{list-style:none;margin:18px 0 0 18px}
  .member{display:flex;gap:12px;position:relative;margin-bottom:20px}
  .member:not(:last-child)::after{content:"";position:absolute;left:15px;top:36px;height:16px;border-left:1px dashed var(--white)}
  .avatar{flex:none;width:32px;height:32px;border-radius:50%;background:var(--grey-avatar);position:relative;overflow:hidden}
  .avatar::before{content:"";position:absolute;left:11px;top:7px;width:10px;height:10px;border-radius:50%;background:#9b9b9b}
  .avatar::after{content:"";position:absolute;left:6px;top:19px;width:20px;height:16px;border-radius:10px 10px 0 0;background:#9b9b9b}
  .member h3{font-size:8.5px;font-weight:700;text-decoration:underline;margin-bottom:3px}
  .member p{font-size:6.5px;line-height:1.4;color:#ddd}
  .divider{width:190px;height:1px;background:var(--white);margin:14px 0 0 110px}
  .contact{position:absolute;left:20px;bottom:26px}
  .contact h2{font-size:15px;font-weight:700;color:var(--red);text-decoration:underline;margin-bottom:10px}
  .contact li{list-style:none;font-size:9px;display:flex;align-items:center;gap:8px;margin-bottom:7px}
  .dot{width:9px;height:9px;border-radius:50%;background:var(--red);flex:none}
  .social{position:absolute;right:22px;bottom:90px;display:flex;align-items:center;gap:6px;font-size:10px}
  .social .dot{width:11px;height:11px}

  /* front panel */
  .front{background:var(--white)}
  .front-band{position:absolute;left:0;right:0;top:200px;bottom:0;background:var(--red)}
  .brand{position:absolute;top:36px;left:0;right:0;text-align:center;color:var(--navy);font-weight:700;font-size:26px;line-height:1}
  .brand small{display:block;font-size:10px;letter-spacing:8px;margin-top:6px}
  .cover-photo{position:absolute;left:72px;top:108px;width:246px;height:246px;border-radius:50%;border:5px solid var(--white);box-shadow:0 0 0 1px var(--red);background:radial-gradient(circle at 45% 45%,#c9a58a 0%,#7c6a5e 35%,#3f4b52 70%,#2c3338 100%)}
  .chevron{position:absolute;left:186px;top:368px}
  .heading{position:absolute;left:0;right:0;top:388px;text-align:center;font-family:"Oswald",sans-serif;font-weight:700;font-size:40px;color:var(--white);letter-spacing:.5px}
  .web{position:absolute;left:0;right:0;top:458px;display:flex;align-items:center;justify-content:center;gap:12px;color:var(--white);font-size:10px;letter-spacing:3px}
  .web::before,.web::after{content:"";width:80px;height:1px;background:var(--white)}

  /* inside */
  .inside{background:var(--paper)}
  .inside + .inside{background:#fafafa}
  .ghost-brand{position:absolute;left:0;right:0;top:160px;text-align:center;color:var(--navy);opacity:.06;font-weight:700;font-size:40px}
  .ghost-brand small{display:block;font-size:14px;letter-spacing:12px}
  .pocket{position:absolute;left:14px;right:14px;bottom:0;height:150px;background:var(--ink);border-radius:18px 18px 0 0}
  .pocket-note{position:absolute;left:0;right:0;top:64px;text-align:center;color:var(--white);font-size:12px;letter-spacing:.5px}
  .card-slot{position:absolute;left:96px;top:-40px;width:170px;height:100px;background:var(--red);display:flex;align-items:center;justify-content:center;flex-direction:column;box-shadow:0 3px 8px rgba(0,0,0,.35)}
  .card-slot .card-band{width:100%;height:40px;background:var(--white);display:flex;flex-direction:column;align-items:center;justify-content:center;color:var(--navy);font-weight:700;font-size:12px}
  .card-slot .card-band small{font-size:5px;letter-spacing:3px}
  .card-slot .card-web{color:var(--white);font-size:5.5px;margin-top:8px;letter-spacing:.5px}
</style>
</head>
<body>

<section class="spread spread--outside">
  <div class="panel back">
    <span class="team-tag">5 MEMBERS OF THE TEAM</span>
    <ul class="team-list">
      <li class="member"><span class="avatar"></span><div><h3>TEXT GOES HERE</h3><p>Lorem Ipsum is simply dummy text of the printing and typesetting industry. Lorem Ipsum has been the industry's standard dummy text ever since the 1500s.</p></div></li>
      <li class="member"><span class="avatar"></span><div><h3>TEXT GOES HERE</h3><p>Lorem Ipsum is simply dummy text of the printing and typesetting industry. Lorem Ipsum has been the industry's standard dummy text ever since the 1500s.</p></div></li>
      <li class="member"><span class="avatar"></span><div><h3>TEXT GOES HERE</h3><p>Lorem Ipsum is simply dummy text of the printing and typesetting industry. Lorem Ipsum has been the industry's standard dummy text ever since the 1500s.</p></div></li>
      <li class="member"><span class="avatar"></span><div><h3>TEXT GOES HERE</h3><p>Lorem Ipsum is simply dummy text of the printing and typesetting industry. Lorem Ipsum has been the industry's standard dummy text ever since the 1500s.</p></div></li>
      <li class="member"><span class="avatar"></span><div><h3>TEXT GOES HERE</h3><p>Lorem Ipsum is simply dummy text of the printing and typesetting industry. Lorem Ipsum has been the industry's standard dummy text ever since the 1500s.</p></div></li>
    </ul>
    <div class="divider"></div>
    <div class="social">Visit Us On : <span class="dot"></span><span class="dot"></span><span class="dot"></span><span class="dot"></span></div>
    <div class="contact">
      <h2>GET IN TOUCH</h2>
      <ul>
        <li><span class="dot"></span>Address Goes Here</li>
        <li><span class="dot"></span>Phone No Goes Here</li>
        <li><span class="dot"></span>Email Address Goes Here</li>
        <li><span class="dot"></span>Web Address Goes Here</li>
      </ul>
    </div>
  </div>

  <div class="panel front">
    <div class="front-band"></div>
    <div class="brand">Harrowgate<small>GROUP</small></div>
    <div class="cover-photo" role="img" aria-label="Photo: a hand passing house keys to an open palm"></div>
    <svg class="chevron" width="18" height="10" viewBox="0 0 18 10"><polyline points="1,1 9,8 17,1" fill="none" stroke="#fff" stroke-width="1.5"/></svg>
    <h1 class="heading">HEADING GOES HERE</h1>
    <div class="web">www.webaddress.com</div>
  </div>
</section>
<div class="view-label view-label--outside">OUTSIDE</div>

<section class="spread spread--inside">
  <div class="panel inside">
    <div class="ghost-brand">Harrowgate<small>GROUP</small></div>
    <div class="pocket"><p class="pocket-note">A GROUP PHOTO GOES HERE</p></div>
  </div>
  <div class="panel inside">
    <div class="ghost-brand">Harrowgate<small>GROUP</small></div>
    <div class="pocket">
      <div class="card-slot">
        <div class="card-band">Harrowgate<small>GROUP</small></div>
        <div class="card-web">WEB ADDRESS GOES HERE</div>
      </div>
    </div>
  </div>
</section>
<div class="view-label view-label--inside">INSIDE</div>

</body>
</html>
```